Upmarket designer fashion & gift boutique card design

I need a business card that captures the vision of my customer & store. I am a ladies fashion boutique in the beautiful Northern Beaches of Sydney. I stock top australian designer fashion that is bold, colourful, & eccentric. My store also carries quirky & retro gift ware & unique statement jewellery. I want a card that is as colourful & eccentric as the designers I stock & the customer I attract. I love bold bright colours, leopard print, abstract or geometric shapes but nothing to fluffy or girly. I have attached my logo which is to be included on one side of the card.

Target Market(s)

25+ with a strong focus on the fabulous 30's & 40's

Industry/Entity Type

Boutique

Contact Information for Business Card

Delia Marchbank, Director, Shop 5/17 Wattlecrest Lane Coralvale NSW 2196, delia@tulvatulva.com.au ABN 61 307 594 218, mobile number 0482 716 053 www.facebook.com/tulvatulva

Font styles to use
Sans Serif

Colors

Designer to choose colors to be used in the design.

Requirements
Must have
• Open mind- although leopard or zebra print would win some votes
Nice to have
• Unique, fun,bold, quirky & different - hit me with your best shot!
Should not have
• No swirly/running writing text please

```html
<!DOCTYPE html>
<html lang="en">
<head>
<meta charset="utf-8">
<title>Saffron Row – Business Card Front</title>
<link rel="stylesheet" href="https://fonts.googleapis.com/css2?family=Work+Sans:wght@600&display=swap">
<style>
  :root {
    --paper: #ffffff;
    --ink: #1c1c1c;
    --gold-dark: #9a7422;
    --gold-light: #f6dc8c;
    --band-green: #3fb54a;
    --band-yellow: #f2d11e;
    --band-orange: #ef861c;
    --band-red: #df2a26;
    --band-pink: #de2a82;
    --band-purple: #8b43a3;
    --band-blue: #2c3c9e;
  }
  html, body {
    margin: 0;
    padding: 0;
    overflow: hidden;
    background: var(--paper);
  }
  .card {
    position: relative;
    width: 1200px;
    height: 741px;
    background: var(--paper);
    overflow: hidden;
  }
  .print-band {
    position: absolute;
    left: 0;
    width: 100%;
    background: linear-gradient(90deg,
      var(--band-green) 0%,
      var(--band-yellow) 22%,
      var(--band-orange) 38%,
      var(--band-red) 54%,
      var(--band-pink) 70%,
      var(--band-purple) 85%,
      var(--band-blue) 100%);
  }
  .print-band--top { top: 0; height: 111px; }
  .print-band--bottom { top: 640px; height: 101px; }
  .gold-rule {
    position: absolute;
    left: 0;
    width: 100%;
    height: 15px;
    background: linear-gradient(90deg,
      var(--gold-dark) 0%,
      var(--gold-light) 30%,
      var(--gold-dark) 55%,
      var(--gold-light) 80%,
      var(--gold-dark) 100%);
  }
  .gold-rule--top { top: 111px; }
  .gold-rule--bottom { top: 625px; }
  .brand-name {
    position: absolute;
    left: 0;
    top: 318px;
    width: 100%;
    margin: 0;
    text-align: center;
    font-family: "Work Sans", sans-serif;
    font-weight: 600;
    font-size: 92px;
    line-height: 100px;
    letter-spacing: 4px;
    text-transform: uppercase;
    color: var(--ink);
  }
</style>
</head>
<body>
  <main class="card">
    <div class="print-band print-band--top" role="img" aria-label="Rainbow zebra-stripe print band"></div>
    <div class="gold-rule gold-rule--top"></div>

    <h1 class="brand-name">Saffron Row</h1>

    <div class="gold-rule gold-rule--bottom"></div>
    <div class="print-band print-band--bottom" role="img" aria-label="Rainbow zebra-stripe print band"></div>
  </main>
</body>
</html>
```